Marn-ridge Tide Harbor Custom Brokers Limited

Name: Dorvella Hastings
Title: Customs Broker
Address: Shop 9 Birchfield Commercial Complex
207-209 Harlow Road
Kingston 8
Telephone: (876)
Email: tideharborport@quillmail.example

```html
<!DOCTYPE html>
<html lang="en">
<head>
<meta charset="UTF-8">
<title>Marn-ridge Tide Harbor Custom Brokers Limited – Business Card</title>
<link href="https://fonts.googleapis.com/css2?family=Poppins:wght@300;400;600;700&display=swap" rel="stylesheet">
<style>
  :root {
    --navy: #0d3a73;
    --navy-deep: #0a2f5e;
    --gold: #f2c511;
    --paper: #f4f5f6;
    --grey: #8d9399;
    --white: #ffffff;
    --stage: #e6e8eb;
  }
  * { margin: 0; padding: 0; box-sizing: border-box; }
  html, body { width: 1200px; height: 780px; overflow: hidden; }
  body {
    background: var(--stage);
    font-family: "Poppins", sans-serif;
    position: relative;
  }
  .card {
    position: absolute;
    top: 235px;
    width: 540px;
    height: 309px;
    border-radius: 4px;
    overflow: hidden;
    box-shadow: 0 10px 30px rgba(0,0,0,0.18);
  }
  .card--front { left: 40px; background: var(--paper); }
  .card--back {
    left: 620px;
    background: radial-gradient(ellipse at 50% 45%, #134787 0%, var(--navy) 55%, var(--navy-deep) 100%);
  }
  .card__shape { position: absolute; inset: 0; }

  .brand {
    position: absolute;
    display: flex;
    align-items: center;
    gap: 12px;
  }
  .brand__mark {
    width: 34px; height: 34px; border-radius: 50%;
    flex: none;
  }
  .brand__name {
    font-weight: 700;
    font-size: 17px;
    line-height: 1.15;
    letter-spacing: 0.5px;
    text-transform: uppercase;
  }
  .brand__sub {
    display: block;
    font-weight: 400;
    font-size: 10.5px;
    letter-spacing: 3px;
    margin-top: 5px;
    text-transform: none;
  }
  .card--front .brand { left: 28px; top: 118px; }
  .card--front .brand__mark { background: var(--navy); }
  .card--front .brand__name { color: var(--navy); }
  .card--front .brand__sub { color: var(--grey); }

  .card--back .brand { left: 50%; top: 50%; transform: translate(-50%, -50%); }
  .card--back .brand__mark { background: var(--gold); }
  .card--back .brand__name { color: var(--white); }
  .card--back .brand__sub { color: var(--white); }

  .contact {
    position: absolute;
    left: 300px;
    top: 52px;
    width: 225px;
    color: var(--white);
  }
  .contact__name {
    font-weight: 700;
    font-size: 16px;
    text-transform: uppercase;
    letter-spacing: 0.3px;
  }
  .contact__title {
    color: var(--gold);
    font-size: 12px;
    font-weight: 400;
    margin-bottom: 20px;
  }
  .contact__row {
    display: flex;
    align-items: flex-start;
    gap: 9px;
    font-size: 10px;
    line-height: 1.45;
    margin-bottom: 11px;
    font-weight: 300;
  }
  .contact__icon {
    width: 16px; height: 16px; flex: none;
    border-radius: 50%;
    background: var(--gold);
    display: flex; align-items: center; justify-content: center;
    margin-top: 1px;
  }
  .contact__icon svg { width: 9px; height: 9px; }
</style>
</head>
<body>

<section class="card card--front" aria-label="Business card front">
  <svg class="card__shape" viewBox="0 0 540 309" preserveAspectRatio="none" aria-hidden="true">
    <path d="M262 0 C246 120 248 230 212 309 L290 309 C262 230 260 120 274 0 Z" fill="var(--gold)"/>
    <path d="M278 0 C264 120 266 230 292 309 L540 309 L540 0 Z" fill="var(--navy)"/>
  </svg>

  <div class="brand">
    <span class="brand__mark"></span>
    <p class="brand__name">Marn-ridge<br>Tide Harbor<span class="brand__sub">Custom Brokers Ltd.</span></p>
  </div>

  <div class="contact">
    <p class="contact__name">Dorvella Hastings</p>
    <p class="contact__title">Customs Broker</p>
    <p class="contact__row">
      <span class="contact__icon"><svg viewBox="0 0 10 10"><path d="M2 1 L4 1 L4.6 3 L3.5 3.8 C4 5 5 6 6.2 6.5 L7 5.4 L9 6 L9 8 C9 8.6 8.5 9 8 9 C4.5 9 1 5.5 1 2 C1 1.5 1.4 1 2 1 Z" fill="var(--navy)"/></svg></span>
      (876) 555 014 2287
    </p>
    <p class="contact__row">
      <span class="contact__icon"><svg viewBox="0 0 10 10"><rect x="1" y="2.2" width="8" height="5.6" rx="0.6" fill="var(--navy)"/><path d="M1.3 2.6 L5 5.4 L8.7 2.6" stroke="var(--gold)" stroke-width="0.8" fill="none"/></svg></span>
      tideharborport@quillmail.example
    </p>
    <p class="contact__row">
      <span class="contact__icon"><svg viewBox="0 0 10 10"><path d="M5 9.5 C3 7 2 5.4 2 4 A3 3 0 0 1 8 4 C8 5.4 7 7 5 9.5 Z" fill="var(--navy)"/><circle cx="5" cy="4" r="1.1" fill="var(--gold)"/></svg></span>
      Shop 9 Birchfield Commercial Complex<br>207-209 Harlow Road, Kingston 8
    </p>
  </div>
</section>

<section class="card card--back" aria-label="Business card back">
  <div class="brand">
    <span class="brand__mark"></span>
    <p class="brand__name">Marn-ridge<br>Tide Harbor<span class="brand__sub">Custom Brokers Ltd.</span></p>
  </div>
</section>

</body>
</html>
```